Couples Workshop Flyer

I need a flyer to promote a one-day workshop for couples.

I am a therapist and life-coach and the session is called: "Lantern Pairs Rising, and bring out the best in each other' - so Lantern Pairs Rising is the bold name for the seminar but the point of the whole workshop is in the tagline, 'and bring out the best in each other'.

The final design should compel couples to take the risk to leave their comfort zones and attend a one-day workshop on a weekend .

Target Market(s)

Couples who are interested in self-improvement and identify with change and growth.
Somehow the flyer will match their aspirations!

Requirements
Should not have
• Not too many love hearts! :)
Not too gushy - a hint of romance!

```html
<!DOCTYPE html>
<html lang="en">
<head>
<meta charset="utf-8">
<title>Lantern Pairs Rising – One-Day Couples Seminar</title>
<link rel="stylesheet" href="https://fonts.googleapis.com/css2?family=Open+Sans:wght@400;600;700&display=swap">
<style>
  :root {
    --wine: #a52d42;
    --wine-light: #b23c51;
    --wine-soft: #ad3549;
    --wine-deep: #6a1f2c;
    --blush: #e9d4d6;
    --white: #ffffff;
    --photo-top: #cfd9b8;
    --photo-mid: #e7d2c0;
    --photo-low: #f2e6dc;
  }
  html, body {
    margin: 0;
    padding: 0;
    width: 1200px;
    height: 2588px;
    overflow: hidden;
    background: var(--white);
  }
  .flyer {
    position: relative;
    width: 1200px;
    height: 2588px;
    overflow: hidden;
    font-family: "Open Sans", Arial, sans-serif;
    color: var(--white);
    text-align: center;
  }
  .flyer__backdrop {
    position: absolute;
    inset: 0;
    width: 1200px;
    height: 2588px;
  }
  .flyer__block {
    position: absolute;
    left: 0;
    width: 1200px;
    margin: 0;
  }
  .title {
    top: 895px;
    font-size: 73px;
    font-weight: 600;
    line-height: 1.2;
  }
  .tagline {
    top: 1000px;
    font-size: 39px;
    font-weight: 400;
  }
  .divider {
    position: absolute;
    top: 1126px;
    left: 209px;
    width: 784px;
    border-top: 3px dotted var(--blush);
    opacity: 0.7;
  }
  .intro {
    top: 1172px;
    left: 220px;
    width: 760px;
    font-size: 28px;
    line-height: 42px;
  }
  .gain__lead {
    top: 1362px;
    font-size: 78px;
    font-weight: 700;
    line-height: 1.2;
  }
  .gain__rest {
    top: 1462px;
    font-size: 56px;
    font-weight: 700;
    line-height: 78px;
  }
  .promise {
    top: 1660px;
    font-size: 42px;
    font-weight: 700;
    line-height: 63px;
  }
  .presenter__label {
    top: 1935px;
    font-size: 29px;
  }
  .presenter__name {
    top: 2012px;
    font-size: 55px;
    font-weight: 700;
    letter-spacing: 3px;
  }
  .presenter__role {
    top: 2095px;
    font-size: 24px;
  }
  .cta__text {
    top: 2380px;
    font-size: 29px;
  }
  .cta__link {
    top: 2438px;
    font-size: 35px;
    font-weight: 700;
  }
</style>
</head>
<body>
<main class="flyer">
  <svg class="flyer__backdrop" viewBox="0 0 1200 2588" xmlns="http://www.w3.org/2000/svg">
    <defs>
      <linearGradient id="photoTone" x1="0" y1="0" x2="1" y2="1">
        <stop offset="0" stop-color="var(--photo-top)"/>
        <stop offset="0.5" stop-color="var(--photo-mid)"/>
        <stop offset="1" stop-color="var(--photo-low)"/>
      </linearGradient>
    </defs>
    <rect class="hero-photo" role="img" aria-label="Photo of a smiling couple leaning together, each holding a glass of white wine, in a sunny garden" x="0" y="0" width="1200" height="820" fill="url(#photoTone)"/>
    <polygon class="hero-edge" points="0,760 1200,540 1200,600 0,830" fill="var(--white)" opacity="0.55"/>
    <polygon class="panel" points="0,810 1200,562 1200,2588 0,2588" fill="var(--wine)"/>
    <polygon class="facet" points="0,810 520,705 340,2588 0,2588" fill="var(--wine-light)" opacity="0.45"/>
    <polygon class="facet" points="780,650 1200,562 1200,1500" fill="var(--wine-soft)" opacity="0.6"/>
    <polygon class="facet" points="520,705 780,650 900,2200 600,2300" fill="var(--wine-soft)" opacity="0.35"/>
    <polygon class="footer-band" points="0,2340 1200,2164 1200,2588 0,2588" fill="var(--wine-deep)"/>
  </svg>

  <h1 class="flyer__block title">Lantern Pairs Rising</h1>
  <p class="flyer__block tagline">and bring out the best in each other</p>
  <div class="divider"></div>
  <p class="flyer__block intro">Some couples spend up big on their wedding day but fail to invest in their marriage or relationship but relationships take much more than love to be successful</p>

  <h2 class="flyer__block gain__lead">What</h2>
  <p class="flyer__block gain__rest">you will gain from<br>Dan's seminar ?</p>
  <p class="flyer__block promise">This innovative one-day seminar<br>helps couples to breathe new life<br>into their relationship</p>

  <p class="flyer__block presenter__label">presenter</p>
  <p class="flyer__block presenter__name">Daniel Marsh</p>
  <p class="flyer__block presenter__role">highly skilled couples therapist and educator</p>

  <p class="flyer__block cta__text">Take your relationship to the next level and book your seat now</p>
  <p class="flyer__block cta__link">http://www.danielmarsh.example/pairs.html</p>
</main>
</body>
</html>
```